Wrap for Porchlight Pals porchlightpals.com

We’re looking for a creative, detail-oriented designer to create a bold, western-themed vehicle wrap for our company, Porchlight Pals (porchlightpals.com | 800-555-0143). The wrap should help our fleet stand out and instantly communicate our fun, professional, “Texas cowboy” brand identity—think red, white, and blue, cowboy hats, stars, boots, and that classic ranch feel!
About Us:
Porchlight Pals is a fast-growing home services company based in Florida, known for reliable repairs, a can-do attitude, and our cowboy-inspired branding. Our mascot and our logo (see attached images) feature a friendly cowboy in overalls, gloves, and a big hat, with colors and style that pop.
What We Need:
A full vehicle wrap design for a work van or truck
Design must incorporate our branding elements:
Our cowboy mascot (see reference images attached)
Our logo (see attached PNG)
Our brand colors: Red, blue, white
Our website (porchlightpals.com) and phone number (800-555-0143) clearly visible
Western/ranch theme throughout: hats, stars, rope details, badge shapes, etc.
Fun, professional, and memorable—NOT cheesy or clip-art
Side, rear, and hood designs (templates provided after award if needed)
Scalable and print-ready file (vector preferred)
References:
[Attach the mascot image, logo PNG, and any sample vehicle pics if you have them]
Ideal Designer:
Experience designing vehicle wraps (with portfolio examples)
Skilled at cartoon/mascot illustration and western/retro themes
Able to provide all files needed for print and installation
Deliverables:
Full wrap design (all sides) as scalable vector (AI, EPS, PDF)
Mockup of the design on 2014 Brisco Transit Cargo Van
I have the design templete from Tilo Film files.quarvenshare.net/share/folders/8KpqZ2mTr41LbnVy6HeQw0DfAs3CuJgPk?src=share_link
Print-ready files for wrap company
Home Owners

```html
<!DOCTYPE html>
<html lang="en">
<head>
<meta charset="utf-8">
<title>Porchlight Pals — Van Wrap</title>
<link rel="stylesheet" href="https://fonts.googleapis.com/css2?family=Oswald:wght@600&family=Roboto+Condensed:ital,wght@1,700&family=Arvo:wght@700&display=swap">
<style>
  :root{
    --stage-top:#3a3a3e;
    --stage-bottom:#8c8a90;
    --wrap-blue:#2c3a8e;
    --wrap-blue-deep:#1f2a72;
    --wrap-red:#d3283a;
    --wrap-red-deep:#a91e2c;
    --wrap-white:#f3f3f5;
    --glass:#2a2d33;
    --mascot-skin:#c98a5a;
    --mascot-denim:#3f5fa6;
  }
  *{margin:0;padding:0;box-sizing:border-box}
  html,body{width:1200px;height:3565px;overflow:hidden;background:var(--stage-top)}
  .wrap-sheet{width:1200px;height:3565px;display:flex;flex-direction:column}
  .panel{position:relative;width:1200px;background:linear-gradient(180deg,var(--stage-top),var(--stage-bottom))}
  .panel--side{height:1200px}
  .panel--rear{height:1250px}
  .panel--hood{height:1115px}
  .panel svg{display:block;width:100%;height:100%}
  .brand-name{font-family:"Oswald",sans-serif;font-weight:600;fill:var(--wrap-white)}
  .brand-name--red{fill:var(--wrap-red)}
  .brand-region{font-family:"Arvo",serif;font-weight:700;fill:var(--wrap-white);letter-spacing:4px}
  .phone-line{font-family:"Oswald",sans-serif;font-weight:600;fill:var(--wrap-white)}
  .web-line{font-family:"Roboto Condensed",sans-serif;font-style:italic;font-weight:700;fill:var(--wrap-blue)}
  .web-line--rear{font-family:"Arvo",serif;font-style:normal;fill:var(--wrap-white)}
</style>
</head>
<body>
<main class="wrap-sheet">

  <!-- Side elevation -->
  <section class="panel panel--side">
    <svg viewBox="0 0 1200 1200" xmlns="http://www.w3.org/2000/svg">
      <defs>
        <symbol id="star" viewBox="-1 -1 2 2"><polygon points="0,-1 0.2245,-0.309 0.951,-0.309 0.363,0.118 0.588,0.809 0,0.382 -0.588,0.809 -0.363,0.118 -0.951,-0.309 -0.2245,-0.309" fill="currentColor"/></symbol>
        <clipPath id="side-body"><path d="M40 330 Q40 250 110 245 L860 245 Q900 245 930 290 L1010 420 Q1150 440 1165 520 L1165 720 L40 720 Z"/></clipPath>
      </defs>
      <g clip-path="url(#side-body)">
        <rect x="0" y="200" width="1200" height="560" fill="var(--wrap-blue)"/>
        <polygon points="520,230 780,230 900,760 600,760" fill="var(--wrap-white)"/>
        <polygon points="760,230 1200,230 1200,760 930,760 820,480" fill="var(--wrap-red)"/>
        <polygon points="820,480 930,760 905,760 800,500" fill="var(--wrap-blue)"/>
        <polygon points="300,230 360,230 420,330 370,330" fill="var(--wrap-red)"/>
        <polygon points="360,230 420,230 520,360 470,360" fill="var(--wrap-white)"/>
        <path d="M420 470 Q520 520 560 600 L540 600 Q500 530 410 490 Z" fill="var(--wrap-red)"/>
        <rect x="0" y="245" width="1200" height="18" fill="var(--wrap-red)"/>
      </g>
      <polygon points="735,260 860,260 905,300 975,410 735,410" fill="var(--glass)"/>
      <circle cx="255" cy="720" r="95" fill="var(--stage-bottom)"/>
      <circle cx="1000" cy="720" r="95" fill="var(--stage-bottom)"/>
      <use href="#star" x="60" y="395" width="60" height="60" color="#9aa4d6"/>
      <use href="#star" x="120" y="460" width="34" height="34" color="#9aa4d6"/>
      <use href="#star" x="70" y="490" width="40" height="40" color="#9aa4d6"/>
      <g transform="rotate(6 300 340)">
        <rect x="85" y="270" width="430" height="120" rx="6" fill="var(--wrap-red)" stroke="var(--wrap-white)" stroke-width="6"/>
        <circle cx="118" cy="330" r="12" fill="var(--wrap-white)"/>
        <text class="brand-name" x="300" y="355" font-size="66" text-anchor="middle">Porchlight Pals</text>
        <rect x="170" y="395" width="260" height="46" fill="var(--wrap-blue-deep)" stroke="var(--wrap-white)" stroke-width="3"/>
        <text class="brand-region" x="300" y="428" font-size="28" text-anchor="middle">FLORIDA</text>
        <text class="phone-line" x="300" y="495" font-size="40" text-anchor="middle">(800-555-0143)</text>
      </g>
      <rect x="545" y="240" width="165" height="330" rx="30" fill="var(--mascot-denim)" role="img" aria-label="Cowboy mascot in hat, overalls and tool belt, hands on hips"/>
      <text class="web-line" x="755" y="455" font-size="30" transform="rotate(-3 755 455)">www.porchlightpals.com</text>
    </svg>
  </section>

  <!-- Rear doors -->
  <section class="panel panel--rear">
    <svg viewBox="0 0 1200 1250" xmlns="http://www.w3.org/2000/svg">
      <defs>
        <symbol id="star-r" viewBox="-1 -1 2 2"><polygon points="0,-1 0.2245,-0.309 0.951,-0.309 0.363,0.118 0.588,0.809 0,0.382 -0.588,0.809 -0.363,0.118 -0.951,-0.309 -0.2245,-0.309" fill="currentColor"/></symbol>
        <linearGradient id="rear-fade" x1="0" y1="0" x2="0" y2="1">
          <stop offset="0" stop-color="var(--wrap-blue)"/>
          <stop offset="0.55" stop-color="var(--wrap-red-deep)"/>
          <stop offset="1" stop-color="var(--wrap-blue-deep)"/>
        </linearGradient>
        <clipPath id="rear-body"><path d="M245 170 Q245 110 320 110 L880 110 Q955 110 955 170 L990 1080 L210 1080 Z"/></clipPath>
      </defs>
      <g clip-path="url(#rear-body)">
        <rect x="180" y="100" width="840" height="1000" fill="url(#rear-fade)"/>
        <rect x="180" y="100" width="840" height="510" fill="var(--wrap-white)"/>
        <path d="M180 560 Q600 470 1020 560 L1020 610 Q600 520 180 610 Z" fill="var(--wrap-blue)"/>
        <path d="M180 600 Q600 520 1020 600 L1020 650 Q600 580 180 650 Z" fill="var(--wrap-red)"/>
        <use href="#star-r" x="300" y="760" width="90" height="90" color="#6f5a9c"/>
        <use href="#star-r" x="820" y="760" width="110" height="110" color="#6f5a9c"/>
        <use href="#star-r" x="480" y="860" width="50" height="50" color="#6f5a9c"/>
      </g>
      <line x1="600" y1="110" x2="600" y2="1080" stroke="#1a1a22" stroke-width="4"/>
      <rect x="300" y="170" width="150" height="350" rx="28" fill="var(--mascot-denim)" role="img" aria-label="Cowboy mascot standing, left of logo"/>
      <rect x="750" y="170" width="150" height="350" rx="28" fill="var(--mascot-denim)" role="img" aria-label="Cowboy mascot standing, right of logo"/>
      <rect x="445" y="280" width="310" height="95" rx="5" fill="var(--wrap-red)" stroke="var(--wrap-white)" stroke-width="5"/>
      <text class="brand-name" x="600" y="345" font-size="50" text-anchor="middle">Porchlight Pals</text>
      <rect x="505" y="378" width="190" height="36" fill="var(--wrap-blue-deep)"/>
      <text class="brand-region" x="600" y="404" font-size="22" text-anchor="middle">FLORIDA</text>
      <text class="phone-line" x="305" y="850" font-size="36">800-555-0143</text>
      <rect x="640" y="800" width="190" height="80" rx="8" fill="#1c1c22"/>
      <text class="web-line web-line--rear" x="600" y="990" font-size="38" text-anchor="middle">www.porchlightpals.com</text>
    </svg>
  </section>

  <!-- Hood -->
  <section class="panel panel--hood">
    <svg viewBox="0 0 1200 1115" xmlns="http://www.w3.org/2000/svg">
      <defs>
        <clipPath id="hood-shape"><path d="M200 260 Q600 200 1000 260 L1080 840 Q600 880 120 840 Z"/></clipPath>
      </defs>
      <g clip-path="url(#hood-shape)">
        <rect x="100" y="180" width="1000" height="720" fill="var(--wrap-red)"/>
        <polygon points="470,180 730,180 800,900 400,900" fill="var(--wrap-white)"/>
        <polygon points="440,180 458,180 385,900 365,900" fill="var(--wrap-blue)"/>
        <polygon points="742,180 760,180 835,900 815,900" fill="var(--wrap-blue)"/>
      </g>
      <text class="brand-name brand-name--red" x="600" y="420" font-size="58" text-anchor="middle">Porchlight Pals</text>
    </svg>
  </section>

</main>
</body>
</html>
```